Website for business consultancy - bright and happy feel needed

I need a website with 3/4 pages. I want the first page designed first and the rest will be easy. I need some pictures but none with corporate looking people. I need links to chatterbox and careerweb. I need a contact form. I have samples of websites i like, fonts i like and I need a small logo also. I like simple, clean lines and I want a bright, happy and feminine feel. My audience are small businesses so I don't want them intimidated by new much of a corporate feel.
Updates

Project Deadline Extended Reason: I have not received a design that reflects what I believe the brief to be, therefore I am extending the deadline and increasing the amount to be paid. Added Thursday, October 13, 2016

Target Market(s)

Small medium size businesses who want to grow and need that help but they cannot afford a full time financial director.

Industry/Entity Type

Business Consultant

Number of Pages Required

4 page

Font styles to use
Other font styles liked:
• i can attach images

Colors
fcf0f6
e667a6
85cae6
ffffff
fbee3e

Requirements
Must have
• Link to chatterbox and career web
• Contact form linked to my email
• Pictures - full width images where required
• Colour
• Mobile ready
• Soft feminine feel to it
• I dont want it to look like a corporate business consultancy - much more marketing or interior deign feel
Nice to have
• I would like the 3 services I have in 3 boxes that you click and takes you to a place with more information on the service.
• pictures thinking outside of the box
• Can be wordpress if need be
Should not have
• pictures with too much of a corporate feel
• No pictures of coporate people at all
• i like the following websites
• www.pebblordo.co.uk and others that are attached in the documents with a feminine feel to them

```html
<!DOCTYPE html>
<html lang="en">
<head>
<meta charset="utf-8">
<title>Tessa Marlow Consultancy</title>
<link rel="stylesheet" href="https://fonts.googleapis.com/css2?family=Oswald:wght@300;400&family=Handlee&display=swap">
<style>
:root{
  --blush:#fcf0f6;
  --rose:#e667a6;
  --sky:#85cae6;
  --sun:#fbee3e;
  --white:#ffffff;
  --plum:#8a3f68;
  --photo-rose:#d88ab2;
  --photo-sky:#7db8d4;
  --photo-deep:#9a6a8f;
  --header-band:rgba(230,103,166,.62);
  --overlay:rgba(120,60,100,.22);
  --panel:rgba(230,103,166,.86);
  --field-fill:rgba(252,240,246,.22);
  --field-line:rgba(255,255,255,.7);
}
*{margin:0;padding:0;box-sizing:border-box}
html,body{width:1200px;height:574px;overflow:hidden}
body{position:relative;font-family:'Oswald',sans-serif;font-weight:300;color:var(--white);background:var(--photo-rose)}
.hero-photo{position:absolute;inset:0;background:
  radial-gradient(ellipse 300px 320px at 600px 260px,rgba(252,240,246,.55),transparent 70%),
  radial-gradient(ellipse 280px 360px at 150px 390px,var(--photo-deep),transparent 75%),
  radial-gradient(ellipse 320px 300px at 1050px 420px,var(--photo-sky),transparent 75%),
  linear-gradient(180deg,var(--photo-rose),#c77fa8 55%,#a97aa4)}
.hero-overlay{position:absolute;inset:0;background:var(--overlay)}
.site-header{position:absolute;left:0;top:0;width:1200px;height:90px;background:var(--header-band)}
.brand{position:absolute;left:184px;top:14px;display:flex;align-items:center;gap:12px}
.brand-mark{width:60px;height:60px;border:4px solid var(--white);border-radius:50%}
.brand-name{font-weight:400;font-size:29px;letter-spacing:1px;text-transform:uppercase}
.main-nav a{position:absolute;top:36px;font-size:16px;font-weight:400;color:var(--white);text-decoration:none}
.intro{position:absolute;left:0;width:1200px;text-align:center}
.intro-kicker{top:172px;font-family:'Handlee',cursive;font-size:27px;color:var(--blush)}
.intro-brand{top:222px;font-size:27px;font-weight:400;letter-spacing:1px;text-transform:uppercase}
.intro-lead{top:261px;font-size:17px}
.service{position:absolute;top:330px;width:193px;height:40px;border:2px solid var(--white);font-size:18px;line-height:36px;text-align:center;color:var(--white);text-decoration:none}
.service.is-active{background:var(--rose);border-color:var(--rose)}
.get-in-touch{position:absolute;left:1121px;top:118px;font-family:'Handlee',cursive;font-size:13px}
.touch-arrow{position:absolute;left:1132px;top:136px}
.social a{position:absolute;left:1155px;width:45px;height:50px;font-size:8px;font-weight:400;line-height:50px;text-align:center;text-decoration:none}
.social .friendwall{top:158px;background:var(--rose);color:var(--white)}
.social .chatterbox{top:210px;background:var(--sky);color:var(--white)}
.social .careerweb{top:262px;background:var(--sun);color:var(--plum)}
.pager button{position:absolute;left:0;width:43px;height:47px;border:0;background:var(--blush);display:flex;align-items:center;justify-content:center}
.contact-panel{position:absolute;left:250px;top:499px;width:699px;height:75px;background:var(--panel)}
.contact-title{position:absolute;left:19px;top:20px;font-size:18px;font-weight:400}
.field{position:absolute;top:22px;width:136px;height:23px;border:1px solid var(--field-line);background:var(--field-fill);color:var(--white);font-family:'Oswald',sans-serif;font-size:9px;padding-left:9px}
.field::placeholder{color:var(--white)}
.submit{position:absolute;left:543px;top:22px;width:136px;height:23px;border:0;background:var(--sun);color:var(--plum);font-family:'Oswald',sans-serif;font-size:13px}
.copyright{position:absolute;left:21px;top:538px;font-family:Arial,sans-serif;font-size:10px}
.slide-number{position:absolute;left:1168px;top:541px;font-family:Arial,sans-serif;font-size:10px}
</style>
</head>
<body>
<div class="hero-photo" role="img" aria-label="Photo of a smiling woman in conversation across a desk in a bright office"></div>
<div class="hero-overlay"></div>

<header class="site-header">
  <div class="brand"><span class="brand-mark"></span><span class="brand-name">Tessa Marlow</span></div>
  <nav class="main-nav">
    <a href="#" style="left:667px">Marketing</a>
    <a href="#" style="left:755px">Finance</a>
    <a href="#" style="left:828px">Business Consulting</a>
    <a href="#" style="left:972px">Contact</a>
  </nav>
</header>

<p class="intro intro-kicker">We Offer</p>
<p class="intro intro-brand">Tessa Marlow</p>
<p class="intro intro-lead">Neque porro quisquam est qui dolorem ipsum quia dolor sit amet, consectetur, adipisci velit...</p>

<a class="service is-active" href="#" style="left:296px">Business Coach &amp; Mentor</a>
<a class="service" href="#" style="left:503px">Containing Lorem Ipsum</a>
<a class="service" href="#" style="left:710px">Distribution of letters</a>

<p class="get-in-touch">Get in touch</p>
<svg class="touch-arrow" width="20" height="24" viewBox="0 0 20 24"><path d="M3 1 Q1 14 17 20" fill="none" stroke="#fff" stroke-width="1.3"/><path d="M11 21 L17 20 L15 14" fill="none" stroke="#fff" stroke-width="1.3"/></svg>
<nav class="social">
  <a class="friendwall" href="#">friendwall</a>
  <a class="chatterbox" href="#">chatterbox</a>
  <a class="careerweb" href="#">careerweb</a>
</nav>

<div class="pager">
  <button style="top:400px" aria-label="Next slide"><svg width="12" height="18" viewBox="0 0 12 18"><path d="M2 2 L10 9 L2 16" fill="none" stroke="var(--rose)" stroke-width="2"/></svg></button>
  <button style="top:450px" aria-label="Previous slide"><svg width="12" height="18" viewBox="0 0 12 18"><path d="M10 2 L2 9 L10 16" fill="none" stroke="var(--rose)" stroke-width="2"/></svg></button>
</div>

<form class="contact-panel">
  <p class="contact-title">Contact Form</p>
  <input class="field" style="left:114px" placeholder="Name">
  <input class="field" style="left:258px" placeholder="Email">
  <input class="field" style="left:401px" placeholder="Message">
  <button class="submit" type="button">Submit</button>
</form>

<p class="copyright">©&nbsp; Copyright 2016, www.companyname.com</p>
<p class="slide-number">M1</p>
</body>
</html>
```